Web Pages Improvement, Update of existing MIRB website

Redesign existing website www.mirb.asn.au The # of pages can be reduced to a total of 6 including the home page. We have a design project out for the logo for this site so feel free to bid for that also.
As this is a simple brief with basic pages, we expect the end result to be code ready for uploaded to our existing host.

```html
<!DOCTYPE html>
<html lang="en">
<head>
<meta charset="utf-8">
<title>MIRB – Home</title>
<link rel="stylesheet" href="https://fonts.googleapis.com/css2?family=Source+Sans+3:wght@400;600;700&display=swap">
<style>
:root{
  --orange:#f58220;
  --orange-dark:#ef6c0a;
  --orange-light:#f9a04a;
  --ink:#222;
  --text:#444;
  --muted:#777;
  --line:#c8c8c8;
  --topbar:#ececec;
  --panel:#f1f1f1;
  --footer:#262626;
  --footer-text:#a8a8a8;
  --footer-head:#e4e4e4;
}
*{margin:0;padding:0;box-sizing:border-box}
html,body{width:824px;height:1200px;overflow:hidden}
body{position:relative;background:#fff;font-family:"Source Sans 3",Arial,sans-serif;color:var(--text)}
a{color:inherit;text-decoration:none}
.abs{position:absolute}

.topbar{left:0;top:0;width:824px;height:22px;background:var(--topbar)}
.toplinks{right:39px;top:5px;font-size:10px;color:#222}
.toplinks span{margin:0 4px;color:#555}

.brand{left:25px;top:38px;font-size:46px;font-weight:700;color:var(--orange);letter-spacing:2px;line-height:1}
.search{left:581px;top:67px;width:169px;height:21px;border:1px solid #ddd;box-shadow:0 2px 3px rgba(0,0,0,.15);font-size:10.5px;color:#999;padding:3px 8px}
.search-btn{left:750px;top:67px;width:26px;height:21px;background:var(--orange)}

.nav{left:0;top:113px;width:824px;height:48px;background:linear-gradient(var(--orange-light),var(--orange) 45%,var(--orange-dark))}
.nav a{position:absolute;top:18px;font-size:12.5px;color:#fff;letter-spacing:.2px}
.nav svg{position:absolute;left:0;top:0}

.hero{left:13px;top:163px;width:799px;height:242px;border:1px solid #bbb;background:linear-gradient(90deg,#fafafa,#eef0f1 45%,#e6e9ea)}
.hero-photo{left:362px;top:0;width:436px;height:240px;background:linear-gradient(100deg,#eef2f3 0%,#a9ccd6 30%,#4b8ea1 60%,#2d5f73 100%)}
.hero h1{left:24px;top:37px;font-size:19px;font-weight:400;color:var(--ink)}
.hero p{left:26px;top:66px;width:330px;font-size:9.5px;line-height:15px;color:#333}
.hero-btn{height:18px;width:138px;background:linear-gradient(var(--orange-light),var(--orange-dark));border-radius:3px;color:#fff;font-size:11px;line-height:18px;padding-left:20px}
.hero-btn::before{content:"›";position:absolute;left:7px;top:-1px;font-weight:700;font-size:14px}
.dots{left:11px;top:216px;display:flex;gap:1px}
.dots i{width:8px;height:8px;background:var(--orange)}

.sidebar-bg{left:566px;top:412px;width:258px;height:506px;background:linear-gradient(90deg,#ececec,#fafafa 40%,#f6f6f6)}

.h2{font-size:18px;font-weight:400;color:var(--ink)}
.h2 em{font-style:normal;color:var(--orange)}
.rule{height:1px;background:var(--line)}
.body-copy{font-size:9.4px;line-height:15px;color:#333}
.body-copy p{margin-bottom:5px}

.thumb{height:84px;border:1px solid #999}
.card-title{font-size:11px;line-height:15px;color:var(--orange)}
.card-text{font-size:9.6px;line-height:14.5px;color:#444;text-decoration:underline;text-decoration-color:#aaa}
.more{height:19px;background:#eee;border-radius:3px;font-size:9.5px;line-height:19px;padding-left:7px;color:#333;box-shadow:0 1px 1px rgba(0,0,0,.15)}
.more b{color:var(--orange);margin-left:5px}
.vdiv{left:269px;top:680px;height:220px;border-left:1px dotted #bbb}

.side-h{font-size:14px;color:var(--ink)}
.services{left:586px;top:464px;width:196px;list-style:none}
.services li{height:20.5px;font-size:9.5px;line-height:20.5px;padding-left:22px;position:relative;color:#333}
.services li:nth-child(odd){background:#e8e8e8}
.services li::before{content:"";position:absolute;left:9px;top:7px;border-left:5px solid var(--orange);border-top:3.5px solid transparent;border-bottom:3.5px solid transparent}
.project{top:730px;width:88px;height:75px;border:2px solid #fff;box-shadow:0 0 2px rgba(0,0,0,.4)}
.viewall{left:725px;top:815px;font-size:10.5px;color:#222}
.badge{top:863px;width:24px;height:24px;background:#111}

.footer{left:0;top:918px;width:824px;height:282px;background:var(--footer)}
.footer h3{position:absolute;top:24px;font-size:14px;font-weight:400;color:var(--footer-head)}
.footer ul{position:absolute;top:58px;list-style:none;font-size:10.5px;line-height:19px;color:var(--footer-text)}
.social{position:absolute;top:60px;width:16px;height:16px;background:#4a78b8;border-radius:2px}
.footer .plain{position:absolute;font-size:10.5px;color:var(--footer-text)}
.footer .plain span{margin:0 4px}
.footer .rule{position:absolute;left:17px;top:219px;width:785px;background:#444}
.copy{position:absolute;top:239px;font-size:9px;color:#8a8a8a}
</style>
</head>
<body>

<header>
  <div class="abs topbar"></div>
  <nav class="abs toplinks"><a href="#">Home</a><span>|</span><a href="#">Sitemap</a><span>|</span><a href="#">Member Log In</a></nav>
  <div class="abs brand">MIRB</div>
  <div class="abs search">search here..</div>
  <div class="abs search-btn">
    <svg width="26" height="21" viewBox="0 0 26 21"><circle cx="12" cy="9" r="4" fill="none" stroke="#fff" stroke-width="2"/><line x1="15" y1="12" x2="18" y2="15" stroke="#fff" stroke-width="2.2"/></svg>
  </div>
  <nav class="abs nav">
    <svg width="824" height="48">
      <g stroke="rgba(255,255,255,.85)" stroke-width="1.5">
        <line x1="122" y1="2" x2="108" y2="46"/><line x1="290" y1="2" x2="276" y2="46"/>
        <line x1="422" y1="2" x2="408" y2="46"/><line x1="547" y1="2" x2="533" y2="46"/>
        <line x1="632" y1="2" x2="618" y2="46"/><line x1="717" y1="2" x2="703" y2="46"/>
      </g>
    </svg>
    <a href="#" style="left:41px">OVERVIEW</a>
    <a href="#" style="left:130px">STATEMENT OF PURPOSE</a>
    <a href="#" style="left:299px">TYPES OF TESTING</a>
    <a href="#" style="left:431px">MEMBER LISTING</a>
    <a href="#" style="left:555px">MEMBERS</a>
    <a href="#" style="left:641px">CONTACT</a>
    <a href="#" style="left:727px">LINKS</a>
  </nav>
</header>

<section class="abs hero">
  <div class="abs hero-photo" role="img" aria-label="Technician adjusting precision testing equipment on a workbench"></div>
  <h1 class="abs">Measurement Inspection Review Board</h1>
  <p class="abs">Brightwire Studio is specialized in handling advanced web projects and the ongoing projects that require permanent maintenance and support .We like challenges and do complete these challenge</p>
  <a class="abs hero-btn" href="#" style="left:26px;top:125px">TESTING SERVICES</a>
  <a class="abs hero-btn" href="#" style="left:174px;top:125px">REPAIR SERVICES</a>
  <a class="abs hero-btn" href="#" style="left:26px;top:154px">OTHE SERVICES</a>
  <a class="abs hero-btn" href="#" style="left:174px;top:154px">EQUIPMENT SERV</a>
  <div class="abs dots"><i></i><i></i><i></i><i></i></div>
</section>

<div class="abs sidebar-bg"></div>

<main>
  <h2 class="abs h2" style="left:19px;top:435px">Welcome to <em>Our Website Main Page</em></h2>
  <div class="abs rule" style="left:19px;top:460px;width:513px"></div>
  <div class="abs body-copy" style="left:19px;top:466px;width:535px">
    <p>Brightwire Studio is a web service company, offering a wide range of services which range from designing and development, that is covering almost all the fields in the best possible way. To be the best we know what and how to present beautifully the working of the client's need and their advantages be highlighted. We act in accordance with the Industry certified processes to deliver the best to our clients all over the world. Over years we have built a strong reputation in providing website design and web development services. Thus, Wanna get ahead in the competition with other websites…. Brightwire Studio provide you with an attractive and most convincing website to enhance your marketing goals.</p>
    <p>The only way to success is through the right path and that's what we provide you. None of the other companies has the result we do. So stick to the best that's how you will be the best don't opt for the second best. Our expertise does not limit itself to web development but also it includes Web Hosting, Search Engine Optimization, E-Commerce. We partner hundreds of organization to enhance their business, marketing and profit goals.</p>
  </div>

  <h2 class="abs h2" style="left:18px;top:640px;font-size:15px">Latest Work &amp; Products</h2>
  <div class="abs rule" style="left:18px;top:665px;width:509px"></div>

  <article>
    <div class="abs thumb" style="left:18px;top:678px;width:229px;background:linear-gradient(90deg,#6f7476,#b9c3cc 45%,#8fa6c2)" role="img" aria-label="Engineer in a hard hat reviewing documents beside electrical panels"></div>
    <h3 class="abs card-title" style="left:18px;top:771px;width:235px;font-weight:400">Brightwire Studio is a professional website design</h3>
    <p class="abs card-text" style="left:18px;top:804px;width:240px">Brightwire Studio is a web service company, offering a wide range of services which range from designing and development, that is covering almost all the fields in the best possible way.</p>
    <a class="abs more" href="#" style="left:18px;top:873px;width:75px">READ MORE<b>›</b></a>
  </article>
  <div class="abs vdiv"></div>
  <article>
    <div class="abs thumb" style="left:289px;top:678px;width:229px;background:linear-gradient(110deg,#d8d4cc,#f2efe8 45%,#e0b08a 70%,#c9c2b3)" role="img" aria-label="Multimeter probes and screwdriver laid on a circuit plan"></div>
    <h3 class="abs card-title" style="left:291px;top:769px;width:235px;font-weight:400">Brightwire Studio is a professional website design</h3>
    <p class="abs card-text" style="left:291px;top:802px;width:240px">Brightwire Studio is a web service company, offering a wide range of services which range from designing and development, that is covering almost all the fields in the best possible way.</p>
    <a class="abs more" href="#" style="left:288px;top:873px;width:74px">READ MORE<b>›</b></a>
  </article>
</main>

<aside>
  <h2 class="abs side-h" style="left:584px;top:432px">Type of Testing &amp; Services</h2>
  <ul class="abs services">
    <li>Your Services or Testing goes here</li><li>Your Testing goes here</li>
    <li>Your Services or Testing goes here</li><li>Your Testing goes here</li>
    <li>Your Services or Testing goes here</li><li>Your Testing goes here</li>
    <li>Your .Services or Testing goes here</li><li>Your Testing goes here</li>
    <li>Your Services or Testing goes here</li><li>Your Testing goes here</li>
  </ul>
  <h2 class="abs side-h" style="left:584px;top:697px">Finished Projects</h2>
  <div class="abs rule" style="left:584px;top:719px;width:200px;background:#ddd"></div>
  <div class="abs project" style="left:584px;background:radial-gradient(circle at 40% 50%,#8fb3c6,#2d4f6b 70%)" role="img" aria-label="Close-up of a circuit board with a processor chip"></div>
  <div class="abs project" style="left:681px;background:radial-gradient(circle at 50% 50%,#7fae6a,#2f4d2e 70%)" role="img" aria-label="Close-up of a green printed circuit board"></div>
  <a class="abs viewall" href="#">VIEW ALL</a>
  <div class="abs badge" style="left:587px;transform:rotate(45deg) scale(.8)"></div>
  <div class="abs badge" style="left:627px;border-radius:50%"></div>
  <svg class="abs" style="left:669px;top:863px" width="26" height="24"><polygon points="13,2 25,23 1,23" fill="none" stroke="#111" stroke-width="2"/></svg>
  <div class="abs badge" style="left:713px;border-radius:50%;background:none;border:3px solid #111"></div>
  <div class="abs badge" style="left:757px;width:28px;height:22px;top:865px"></div>
</aside>

<footer class="abs footer">
  <h3 style="left:28px">Quick Links</h3>
  <ul style="left:31px"><li>Main page</li><li>Our Services</li><li>Overview</li><li>Partners</li><li>Contact</li></ul>
  <ul style="left:122px"><li>Statement of Purposes</li><li>Type of Testings</li><li>Member Listing</li><li>Members</li><li>Links</li></ul>
  <h3 style="left:277px">Services List</h3>
  <ul style="left:277px"><li>Services here</li><li>Your Services</li><li>Any Other Services</li><li>Services here</li><li>Your Services</li><li>Any Services here</li></ul>
  <h3 style="left:437px">Equipments &amp; Support</h3>
  <ul style="left:440px"><li>Services here</li><li>Your Services here</li><li>Any Other Services here</li><li>Services here</li><li>Your Services here</li><li>Any Other Services here</li></ul>
  <h3 style="left:629px">Connect With Us</h3>
  <span class="social" style="left:634px"></span><span class="social" style="left:655px"></span>
  <span class="social" style="left:676px"></span><span class="social" style="left:697px"></span>
  <p class="plain" style="left:634px;top:94px">Circlepage<span>|</span>Searchly</p>
  <p class="plain" style="left:634px;top:113px">Chirper<span>|</span>Workweb</p>
  <div class="rule"></div>
  <p class="copy" style="left:24px">Copyright © 2012 Company Name &nbsp;|&nbsp; All right reserved</p>
  <p class="copy" style="left:640px">Terms &amp; Conditions | Privacy Policy</p>
</footer>

</body>
</html>
```